Website Design for A Nook for Grandpas

Please design and code a new website.
Here are the sites I like best:
http://www.sailbeacon.net/alternate/
http://www.wheelsgiving.net
Please make it similar but look at the competitor site (below) for images and wording. This is NOT a car donation site. It's a senior lead placement site like https://www.eldernestfinder.net. I just like this sites above as a lead generation sites.
Competitor site:
https://www.eldernestfinder.net (use ideas / verbiage from this site)
Updates
Competitor site:

```html
<!DOCTYPE html>
<html lang="en">
<head>
<meta charset="utf-8">
<title>A Nook for Grandpas — Senior Living Search</title>
<link href="https://fonts.googleapis.com/css2?family=Roboto:ital,wght@0,400;0,500;0,700;1,400;1,500&family=Roboto+Condensed:wght@300;700&family=Poppins:wght@400;500&display=swap" rel="stylesheet">
<style>
:root{
  --green:#0f8f45;
  --green-dark:#0a7a3b;
  --lime:#7cbf2f;
  --lime-line:#5cb03a;
  --navy:#0b2f7c;
  --ink:#333;
  --muted:#555;
  --grey-bg:#eef1f0;
  --outer:#ececec;
  --white:#fff;
}
*{box-sizing:border-box;margin:0;padding:0}
html,body{width:1200px;height:3342px;overflow:hidden}
body{background:var(--outer);font-family:'Poppins',sans-serif;color:var(--ink)}
.page{position:absolute;left:83px;top:0;width:1034px;height:3342px;background:var(--white)}
section,header,nav,footer{position:relative;width:1034px}

/* header */
.site-header{height:122px}
.brand{position:absolute;display:flex;align-items:center;gap:10px;font-family:'Roboto',sans-serif;font-weight:400;white-space:nowrap}
.brand-dot{width:30px;height:30px;border-radius:50%;background:var(--lime)}
.site-header .brand{left:92px;top:42px;font-size:30px;color:#3a3a3a}
.call{position:absolute;left:440px;width:228px;top:36px;text-align:right;font-family:'Roboto',sans-serif;white-space:nowrap}
.call small{display:block;font-size:17px;line-height:20px;color:#444}
.call strong{display:block;font-size:22px;line-height:28px;color:#333;font-weight:700}
.phone-ring{position:absolute;left:685px;top:42px;width:40px;height:40px;border:2px solid var(--green);border-radius:50%;display:flex;align-items:center;justify-content:center}
.estimate{position:absolute;left:744px;top:42px;width:204px;height:40px;border:2px solid var(--navy);border-radius:22px;color:var(--navy);font:700 14px 'Roboto',sans-serif;display:flex;align-items:center;justify-content:center}

.main-nav{height:48px;background:var(--navy);display:flex;justify-content:space-between;align-items:center;padding:0 92px;color:#fff;font:500 14px 'Roboto',sans-serif}

/* hero */
.hero{height:589px;overflow:hidden}
.hero-photo{position:absolute;inset:0;background:linear-gradient(100deg,#5e8a44 0%,#7ea25c 35%,#b8b39b 65%,#d9d3c4 100%)}
.hero-copy{position:absolute;left:56px;top:115px;color:#fff}
.hero-copy h1{font:700 28px/40px 'Roboto',sans-serif;text-transform:uppercase}
.hero-copy p{font:400 17px 'Roboto',sans-serif;margin-top:14px}
.field{display:flex;align-items:center;justify-content:center;background:#fff;border:1px solid #ddd;font:400 12px 'Poppins',sans-serif;color:#666}
.hero-copy .field{width:328px;height:44px;margin-top:22px}
.btn{display:flex;align-items:center;justify-content:center;color:#fff;font:700 15px 'Roboto',sans-serif;letter-spacing:.5px}
.hero-copy .btn{width:328px;height:44px;margin-top:14px;background:var(--green)}
.help{font:300 28px 'Roboto Condensed',sans-serif;margin-top:22px}
.help b{font-weight:700}
.dots{display:flex;gap:8px;margin-top:28px;margin-left:0}
.dots span{width:16px;height:16px;border:2px solid #fff;border-radius:50%}
.hero-curve{position:absolute;left:0;bottom:0}

/* intro */
.intro{height:367px;text-align:center}
.intro h2{padding-top:14px;font:italic 400 29px 'Roboto',sans-serif;color:#333}
.intro h2 b,.section-title b{font-style:normal;font-weight:700}
.intro p.lead{width:720px;margin:22px auto 0;font:400 13px/26px 'Poppins',sans-serif;color:#555}
.features{display:flex;justify-content:center;margin-top:36px}
.feature{width:179px;text-align:center;font:400 15px/22px 'Roboto',sans-serif;color:#333}
.feature .ring{width:72px;height:72px;margin:0 auto 12px;border:3px solid var(--green);border-radius:50%;display:flex;align-items:center;justify-content:center}

/* services */
.services{height:586px;background:var(--grey-bg)}
.section-title{text-align:center;font:italic 400 33px 'Roboto',sans-serif;color:#333}
.services .section-title{padding-top:76px}
.rule{width:78px;height:3px;background:var(--green);margin:20px auto 0}
.card{position:absolute;width:275px;background:#fff;box-shadow:0 2px 4px rgba(0,0,0,.12);text-align:center}
.card-photo{position:relative;height:190px}
.card-photo svg{position:absolute;left:0;bottom:0}
.card h3{font:400 18px 'Roboto',sans-serif;color:#222;margin-top:6px}
.card p{font:400 12px/22px 'Poppins',sans-serif;color:#555;padding:12px 16px 24px}

/* advisor */
.advisor{height:461px;background:linear-gradient(180deg,#1a9a4c 0%,#119047 60%,#0c8a44 100%);color:#fff;overflow:hidden}
.advisor-bg{position:absolute;inset:0;background:radial-gradient(ellipse at 50% 45%,rgba(255,255,255,.10),rgba(255,255,255,0) 60%)}
.advisor-top{position:absolute;left:0;top:0}
.advisor h2{position:absolute;top:136px;width:100%;text-align:center;font:italic 400 29px 'Roboto',sans-serif}
.advisor h2 b{font-style:normal;font-weight:700;font-size:36px}
.advisor .sub{position:absolute;top:195px;width:100%;text-align:center;font:400 15px 'Roboto',sans-serif}
.perks{position:absolute;left:180px;top:258px;list-style:none;font:400 15px 'Roboto',sans-serif}
.perks li{display:flex;align-items:center;gap:8px;height:38px}
.advisor .field{position:absolute;left:498px;top:256px;width:375px;height:44px;justify-content:flex-start;padding-left:22px}
.advisor .btn{position:absolute;left:498px;top:314px;width:375px;height:44px;background:var(--lime)}

/* testimonials */
.testimonials{height:609px}
.testimonials .section-title{padding-top:62px}
.testimonials .section-title b{font-size:35px}
.quote{position:absolute;top:249px;width:275px;height:203px;background:#fafafa;border:1px solid #e6e6e6;text-align:center}
.quote.raised{background:#fff;box-shadow:0 4px 10px rgba(0,0,0,.14)}
.avatar{position:absolute;left:50%;top:-52px;margin-left:-50px;width:100px;height:100px;border-radius:50%;border:6px solid #fff;box-shadow:0 0 0 1px #e6e6e6;background:linear-gradient(135deg,#c9b59c,#7d8fa8)}
.quote p{margin-top:60px;padding:0 24px;font:400 12px/22px 'Poppins',sans-serif;color:#555}
.quote cite{display:block;margin-top:10px;font:italic 500 13px 'Roboto',sans-serif;color:#2a5fb0}

/* footer */
.site-footer{height:560px;background:linear-gradient(120deg,#0f8e48 0%,#0b7d55 40%,#0b4f7a 75%,#0e2f82 100%);color:#fff}
.footer-tab{position:absolute;left:296px;top:-43px;width:441px;height:46px;border-radius:70px 70px 0 0;background:linear-gradient(90deg,#0e8a4d,#0b7264)}
.site-footer .brand{left:395px;top:6px;font-size:26px;color:#fff}
.site-footer .brand-dot{background:#fff}
.col{position:absolute;top:82px}
.col h4{font:700 22px 'Roboto',sans-serif}
.col .bar{width:56px;height:2px;background:#fff;opacity:.8;margin:18px 0 22px}
.col-mail{left:90px}
.input{width:338px;height:32px;border:1px solid rgba(255,255,255,.8);font:400 10px 'Poppins',sans-serif;padding:9px 10px;margin-bottom:10px;color:#fff}
.input.tall{height:56px;padding-top:8px}
.submit{width:166px;height:34px;background:#111;color:#fff;font:700 14px 'Roboto',sans-serif;display:flex;align-items:center;justify-content:center;margin-top:14px}
.col-contact{left:501px}
.c-row{display:flex;gap:14px;font:400 13px/22px 'Roboto',sans-serif;margin-bottom:14px}
.c-icon{flex:none;width:30px;height:30px;border:1.5px solid #fff;border-radius:50%;display:flex;align-items:center;justify-content:center;margin-top:2px}
.socials{display:flex;gap:5px;margin-top:16px;margin-left:6px}
.socials span{width:28px;height:28px;border:1.5px solid #fff;border-radius:50%}
.col-links{left:799px}
.col-links ul{list-style:none;font:400 13px/26px 'Roboto',sans-serif}
.footer-rule{position:absolute;left:0;top:461px;width:1034px;height:1px;background:rgba(255,255,255,.2)}
.copyright{position:absolute;top:498px;width:100%;text-align:center;font:400 13px 'Poppins',sans-serif}
</style>
</head>
<body>
<div class="page">

  <header class="site-header">
    <div class="brand"><span class="brand-dot"></span>A Nook for Grandpas</div>
    <div class="call"><small>Call Us</small><strong>555 0142 7788</strong></div>
    <div class="phone-ring">
      <svg width="18" height="18" viewBox="0 0 24 24"><path d="M6.6 10.8a15 15 0 0 0 6.6 6.6l2.2-2.2a1 1 0 0 1 1-.25 11.4 11.4 0 0 0 3.6.57 1 1 0 0 1 1 1V20a1 1 0 0 1-1 1A17 17 0 0 1 3 4a1 1 0 0 1 1-1h3.5a1 1 0 0 1 1 1c0 1.25.2 2.45.57 3.57a1 1 0 0 1-.25 1z" fill="#0f8f45"/></svg>
    </div>
    <div class="estimate">GET A FREE ESTIMATE!</div>
  </header>

  <nav class="main-nav">
    <span>HOME</span><span>ASSISTED LIVING</span><span>MEMORY CARE</span><span>NURSING HOMES</span><span>PLANNING &amp; ADVICE</span><span>BLOG</span><span>CONTACT US</span>
  </nav>

  <section class="hero">
    <div class="hero-photo" role="img" aria-label="Smiling caregiver leaning over an older man seated in a bright sunroom with a garden outside"></div>
    <div class="hero-copy">
      <h1>You know your family.<br>We know senior living.</h1>
      <p>FIND SENIOR LIVING NEAR YOU.</p>
      <div class="field">Enter city or postal code</div>
      <div class="btn">START YOUR SEARCH</div>
      <div class="help">Need help? <b>Call 555 0142 7788</b></div>
      <div class="dots"><span></span><span></span><span></span></div>
    </div>
    <svg class="hero-curve" width="1034" height="70" viewBox="0 0 1034 70">
      <path d="M0,70 L0,64 Q517,-28 1034,64 L1034,70 Z" fill="#fff"/>
      <path d="M70,60 Q517,-10 964,60" fill="none" stroke="#5cb03a" stroke-width="4"/>
    </svg>
  </section>

  <section class="intro">
    <h2>The support you need to make <b>THE RIGHT CHOICE</b></h2>
    <p class="lead">Sed ut perspiciatis unde omnis iste natus error sit voluptatem accusantium doloremque laudantium, totam rem aperiam, eaque ipsa quae ab illo inventore veritatis et quasi architecto beatae vitae dicta</p>
    <div class="features">
      <div class="feature"><div class="ring"><svg width="34" height="34" viewBox="0 0 34 34"><rect x="4" y="6" width="22" height="22" rx="3" fill="none" stroke="#0f8f45" stroke-width="3"/><path d="M10 17l6 6 14-16" fill="none" stroke="#0f8f45" stroke-width="4"/></svg></div>Dedicated local<br>advisor</div>
      <div class="feature"><div class="ring"><svg width="34" height="34" viewBox="0 0 34 34"><path d="M17 5L3 17h4v12h8v-8h4v8h8V17h4z" fill="#0f8f45"/></svg></div>Hand-picked list of<br>communities to match<br>your needs</div>
      <div class="feature"><div class="ring"><svg width="36" height="36" viewBox="0 0 36 36" fill="none" stroke="#0f8f45" stroke-width="2"><circle cx="20" cy="11" r="7"/><path d="M20 7v8M18 9h3a1.5 1.5 0 0 1 0 3h-2a1.5 1.5 0 0 0 0 3h3"/><path d="M4 26l6-4h7l4 2h-8M10 31l8-1 12-7-2-2-9 4"/></svg></div>Full details and<br>pricing</div>
      <div class="feature"><div class="ring"><svg width="32" height="32" viewBox="0 0 32 32"><rect x="4" y="7" width="24" height="21" rx="2" fill="none" stroke="#0f8f45" stroke-width="2.5"/><rect x="4" y="7" width="24" height="5" fill="#0f8f45"/><path d="M10 4v6M22 4v6" stroke="#0f8f45" stroke-width="2.5"/><g fill="#0f8f45"><rect x="8" y="15" width="4" height="3"/><rect x="14" y="15" width="4" height="3"/><rect x="20" y="15" width="4" height="3"/><rect x="8" y="21" width="4" height="3"/><rect x="14" y="21" width="4" height="3"/><rect x="20" y="21" width="4" height="3"/></g></svg></div>Help scheduling<br>tours</div>
      <div class="feature"><div class="ring"><svg width="32" height="32" viewBox="0 0 32 32" fill="none" stroke="#0f8f45" stroke-width="2"><rect x="6" y="4" width="18" height="24" rx="2"/><circle cx="15" cy="11" r="3"/><path d="M10 19h10M10 23h7M26 10l-6 14"/></svg></div>Move in support</div>
    </div>
  </section>

  <section class="services">
    <h2 class="section-title">OUR <b>SERVICES</b></h2>
    <div class="rule"></div>

    <article class="card" style="left:80px;top:179px">
      <div class="card-photo" role="img" aria-label="Young care worker chatting with an older man by a window" style="background:linear-gradient(120deg,#cfd6d8,#8a97a3 55%,#2d3f6a)">
        <svg width="275" height="26" viewBox="0 0 275 26"><path d="M0,26 L0,24 L137,2 L275,24 L275,26Z" fill="#fff"/><path d="M0,24 L137,2 L275,24" fill="none" stroke="#5cb03a" stroke-width="3"/></svg>
      </div>
      <h3>ASSISTED LIVING</h3>
      <p>Sed ut perspiciatis unde omnis iste natus error sit voluptatem accusantium loremque laudantium, totam rem aperiam</p>
    </article>

    <article class="card" style="left:380px;top:209px">
      <div class="card-photo" role="img" aria-label="Older woman reading a book in a garden" style="background:linear-gradient(120deg,#4f6b3e,#8fa66b 55%,#c9c2ad)">
        <svg width="275" height="26" viewBox="0 0 275 26"><path d="M0,26 L0,24 L137,2 L275,24 L275,26Z" fill="#fff"/><path d="M0,24 L137,2 L275,24" fill="none" stroke="#5cb03a" stroke-width="3"/></svg>
      </div>
      <h3>MEMORY CARE</h3>
      <p>Sed ut perspiciatis unde omnis iste natus error sit voluptatem accusantium loremque laudantium, totam rem aperiam</p>
    </article>

    <article class="card" style="left:678px;top:179px">
      <div class="card-photo" role="img" aria-label="Nurse helping an older man with a tablet in a kitchen" style="background:linear-gradient(120deg,#1f6fc4,#8fa9c6 55%,#d8dce2)">
        <svg width="275" height="26" viewBox="0 0 275 26"><path d="M0,26 L0,24 L137,2 L275,24 L275,26Z" fill="#fff"/><path d="M0,24 L137,2 L275,24" fill="none" stroke="#5cb03a" stroke-width="3"/></svg>
      </div>
      <h3>NURSING HOMES</h3>
      <p>Sed ut perspiciatis unde omnis iste natus error sit voluptatem accusantium loremque laudantium, totam rem aperiam</p>
    </article>
  </section>

  <section class="advisor">
    <div class="advisor-bg" role="img" aria-label="Faint green-tinted photo of a caregiver with an older couple"></div>
    <svg class="advisor-top" width="1034" height="70" viewBox="0 0 1034 70">
      <path d="M0,0 L1034,0 Q517,118 0,0Z" fill="#eef1f0"/>
      <path d="M70,6 Q517,110 964,6" fill="none" stroke="#7cbf2f" stroke-width="3"/>
    </svg>
    <h2>Your <b>LOCAL ADVISOR</b> INFORMS. YOU DECIDE.</h2>
    <p class="sub">Over 400 senior advisors across the U.S. and Canada are ready to help your family with:</p>
    <ul class="perks">
      <li><svg width="12" height="12" viewBox="0 0 12 12"><circle cx="6" cy="6" r="5" fill="none" stroke="#fff" stroke-width="1.2"/><path d="M5 3.5L7.5 6 5 8.5" fill="none" stroke="#fff" stroke-width="1.2"/></svg>Insider's tips for the area near you</li>
      <li><svg width="12" height="12" viewBox="0 0 12 12"><circle cx="6" cy="6" r="5" fill="none" stroke="#fff" stroke-width="1.2"/><path d="M5 3.5L7.5 6 5 8.5" fill="none" stroke="#fff" stroke-width="1.2"/></svg>Advice tailored to your unique situation</li>
      <li><svg width="12" height="12" viewBox="0 0 12 12"><circle cx="6" cy="6" r="5" fill="none" stroke="#fff" stroke-width="1.2"/><path d="M5 3.5L7.5 6 5 8.5" fill="none" stroke="#fff" stroke-width="1.2"/></svg>Time saving know-how and resources</li>
    </ul>
    <div class="field">Enter city or postal code</div>
    <div class="btn">START YOUR SEARCH</div>
  </section>

  <section class="testimonials">
    <h2 class="section-title"><b>98%</b> of our customers recommend our service</h2>
    <div class="rule" style="margin-top:28px"></div>

    <blockquote class="quote" style="left:91px">
      <div class="avatar" role="img" aria-label="Portrait of an older man in a blue shirt"></div>
      <p>Sed ut perspiciatis unde omnis iste natus error sit voluptatem accusantium doloremque laudantium, totam rem aperiam, eaque ipsa quae ab</p>
      <cite>Delgado, R.</cite>
    </blockquote>
    <blockquote class="quote raised" style="left:380px">
      <div class="avatar" role="img" aria-label="Portrait of a smiling older couple" style="background:linear-gradient(135deg,#6b4a30,#c59a66)"></div>
      <p>Sed ut perspiciatis unde omnis iste natus error sit voluptatem accusantium doloremque laudantium, totam rem aperiam, eaque ipsa quae ab</p>
      <cite>Delgado, R.</cite>
    </blockquote>
    <blockquote class="quote" style="left:668px">
      <div class="avatar" role="img" aria-label="Portrait of a caregiver with an older man" style="background:linear-gradient(135deg,#b58a7a,#d8c8b8)"></div>
      <p>Sed ut perspiciatis unde omnis iste natus error sit voluptatem accusantium doloremque laudantium, totam rem aperiam, eaque ipsa quae ab</p>
      <cite>Delgado, R.</cite>
    </blockquote>
  </section>

  <footer class="site-footer">
    <div class="footer-tab"></div>
    <div class="brand"><span class="brand-dot"></span>A Nook for Grandpas</div>

    <div class="col col-mail">
      <h4>E-MAIL US</h4><div class="bar"></div>
      <div class="input">First Name</div>
      <div class="input">Email Address</div>
      <div class="input">Phone Number</div>
      <div class="input tall">Message :</div>
      <div class="submit">SUBMIT</div>
    </div>

    <div class="col col-contact">
      <h4>CONTACT US</h4><div class="bar"></div>
      <div class="c-row"><span class="c-icon"><svg width="14" height="14" viewBox="0 0 24 24"><path d="M12 2a7 7 0 0 0-7 7c0 5 7 13 7 13s7-8 7-13a7 7 0 0 0-7-7zm0 9.5A2.5 2.5 0 1 1 12 6.5a2.5 2.5 0 0 1 0 5z" fill="#fff"/></svg></span><span>27 Maple Grove Lane<br>Suite 410<br>Riverton, Ohio 45012</span></div>
      <div class="c-row"><span class="c-icon"><svg width="14" height="14" viewBox="0 0 24 24"><path d="M6.6 10.8a15 15 0 0 0 6.6 6.6l2.2-2.2a1 1 0 0 1 1-.25 11.4 11.4 0 0 0 3.6.57 1 1 0 0 1 1 1V20a1 1 0 0 1-1 1A17 17 0 0 1 3 4a1 1 0 0 1 1-1h3.5a1 1 0 0 1 1 1c0 1.25.2 2.45.57 3.57a1 1 0 0 1-.25 1z" fill="#fff"/></svg></span><span>Phone:<br>555 0142 7788</span></div>
      <div class="c-row"><span class="c-icon"><svg width="14" height="14" viewBox="0 0 24 24" fill="none" stroke="#fff" stroke-width="2"><rect x="3" y="5" width="18" height="14" rx="2"/><path d="M3 7l9 6 9-6"/></svg></span><span>Email:<br>hello@nookforgrandpas.net</span></div>
      <div class="socials"><span></span><span></span><span></span><span></span></div>
    </div>

    <div class="col col-links">
      <h4>QUICK LINKS</h4><div class="bar"></div>
      <ul><li>Home</li><li>About</li><li>Assisted Living</li><li>Memory Care</li><li>Nursing Homes</li><li>Planning &amp; Advice</li><li>Contact Us</li></ul>
    </div>

    <div class="footer-rule"></div>
    <p class="copyright">Copyright © 2019 A Nook for Grandpas. Privacy Policy. All Rights Reserved.</p>
  </footer>

</div>
</body>
</html>
```